Clean, Fresh Business Card Design Needed

We need a business card design for a new business we have taken over called "Bonders and Fixers". We got a logo through this website which i have attached. We are wanting something that is vibrant but clean and fresh. Our business mainly sells glue. Maybe a cool design/slogan on the back? Modern, sleek.

Industry/Entity Type

Business

Contact Information for Business Card

Name: Derek Tamsin, Managing Director. Address: 164 Kowhai Lane, Tauranga 3112, Phone: 07 549 2361 Mobile: 021 634 915 Fax: 07 549 2874 Email: bond.fix@mailvo.co.nz, Web: www.tackbondpro.co.nz

Font styles to use
Serif

Requirements
Must have
• All business card details, logo.
Nice to have
• Design, slogan on back of card

```html
<!DOCTYPE html>
<html lang="en">
<head>
<meta charset="utf-8">
<title>Bonders and Fixers – Business Card</title>
<link rel="stylesheet" href="https://fonts.googleapis.com/css2?family=Cinzel:wght@400&family=Open+Sans:wght@400;700&display=swap">
<style>
  :root {
    --backdrop: #e9e9ea;
    --card: #fbfbfb;
    --navy: #2c2a66;
    --ink: #1d1d1f;
    --ink-soft: #444448;
    --faint: #efefef;
  }
  * { margin: 0; padding: 0; box-sizing: border-box; }
  html, body { width: 1200px; height: 726px; overflow: hidden; }
  body {
    background: var(--backdrop);
    font-family: "Open Sans", Arial, sans-serif;
    color: var(--ink);
    position: relative;
  }
  .card {
    position: absolute;
    top: 208px;
    width: 520px;
    height: 310px;
    background: var(--card);
    border-radius: 4px;
    box-shadow: 0 6px 18px rgba(0,0,0,0.12);
    overflow: hidden;
  }
  .card--front { left: 50px; }
  .card--back { left: 630px; }

  .wordmark {
    display: flex;
    align-items: center;
    gap: 12px;
    font-family: "Cinzel", Georgia, serif;
    font-weight: 400;
    color: var(--ink);
    white-space: nowrap;
  }
  .wordmark__square {
    background: var(--navy);
    border-radius: 5px;
    flex: none;
  }
  .card--front .wordmark {
    position: absolute;
    left: 50%;
    top: 50%;
    transform: translate(-50%, -50%);
    font-size: 30px;
    letter-spacing: 1px;
  }
  .card--front .wordmark__square { width: 52px; height: 52px; }

  .faint-splash {
    position: absolute;
    right: 0;
    top: 0;
    width: 150px;
    height: 200px;
    background: var(--faint);
    border-bottom-left-radius: 90px;
  }

  .card--back .wordmark {
    position: absolute;
    left: 250px;
    top: 26px;
    font-size: 19px;
  }
  .card--back .wordmark__square { width: 38px; height: 38px; border-radius: 4px; }

  .splash-area {
    position: absolute;
    left: 0;
    bottom: 0;
    width: 230px;
    height: 250px;
    background: var(--navy);
    border-top-right-radius: 120px;
  }

  .contact {
    position: absolute;
    left: 262px;
    top: 96px;
    font-size: 12.5px;
    line-height: 1.55;
    color: var(--ink-soft);
  }
  .contact__name { font-weight: 700; font-size: 14px; color: var(--ink); }
  .contact__role { font-size: 10.5px; margin-bottom: 10px; }
  .contact__row { display: flex; align-items: center; gap: 7px; }
  .contact__row + .contact__row { margin-top: 1px; }
  .contact__row--pair { gap: 7px; }
  .contact__address { margin-left: 19px; margin-top: 2px; }
  .icon { width: 12px; height: 12px; fill: var(--navy); flex: none; }
</style>
</head>
<body>

<section class="card card--front" aria-label="Card front">
  <div class="faint-splash" role="img" aria-label="Faint brand splash decoration"></div>
  <div class="wordmark">
    <span class="wordmark__square"></span>
    <span class="wordmark__name">Bonders and Fixers</span>
  </div>
</section>

<section class="card card--back" aria-label="Card back">
  <div class="splash-area" role="img" aria-label="Large navy brand splash decoration"></div>
  <div class="wordmark">
    <span class="wordmark__square"></span>
    <span class="wordmark__name">Bonders and Fixers</span>
  </div>

  <div class="contact">
    <p class="contact__name">Derek Tamsin</p>
    <p class="contact__role">Manager</p>

    <p class="contact__row contact__row--pair">
      <svg class="icon" viewBox="0 0 12 12" aria-hidden="true"><rect x="3" y="0.5" width="6" height="11" rx="1.2"/><rect x="4" y="2" width="4" height="7" fill="#fbfbfb"/></svg>
      <span>021 634 915</span>
      <svg class="icon" viewBox="0 0 12 12" aria-hidden="true" style="margin-left:6px"><rect x="1" y="4" width="10" height="7" rx="1"/><rect x="3" y="0.5" width="6" height="4" fill="none" stroke="#2c2a66"/></svg>
      <span>07 549 2874</span>
    </p>
    <p class="contact__row">
      <svg class="icon" viewBox="0 0 12 12" aria-hidden="true"><path d="M1 4c0-2 2-3 5-3s5 1 5 3l-2 1-1-1.5H4L3 5zM2.5 6h7L11 11H1z"/></svg>
      <span>07 549 2361</span>
    </p>
    <p class="contact__row">
      <svg class="icon" viewBox="0 0 12 12" aria-hidden="true"><rect x="0.5" y="2.5" width="11" height="7"/><path d="M0.5 2.5 6 7l5.5-4.5" fill="none" stroke="#fbfbfb"/></svg>
      <span>bond.fix@mailvo.co.nz</span>
    </p>
    <p class="contact__row">
      <svg class="icon" viewBox="0 0 12 12" aria-hidden="true"><circle cx="6" cy="6" r="5.5"/><path d="M0.5 6h11M6 0.5c-3 3-3 8 0 11M6 0.5c3 3 3 8 0 11" fill="none" stroke="#fbfbfb" stroke-width="0.8"/></svg>
      <span>www.tackbondpro.co.nz</span>
    </p>
    <p class="contact__address">164 Kowhai Lane, Tauranga 3112</p>
  </div>
</section>

</body>
</html>
```